Web Page Template and Logo Design

We are launching a website to sell homewares and would like a logo design, as well as a home page template, and the template for the product pages.

The homewares store is called Brassy Walrus. The homewares we will sell will be edgy and very bright colours. We envisage the theme of the homepage will have hot pink, some blue/ white chinioserie pattern and potentially lime green. We would like the logo to reflect humour and "Brassy Walrus".

The images uploaded reflect the look and feel of the type of people who are our customers - they are not minimalists and they are definitely not into beige!

Target Market(s)

Predominantly women, 30 - 50

Industry/Entity Type

Store

Number of Pages Required

2 page

Font styles to use
Sans Serif

Colors
e34197
acd036
33a6d7

Requirements
Must have
• Template for home page and standard template for other pages;PLEASE NOTE: I have now listed the Brassy Walrus Logo as a separate 2 day listing; a bright, bold, colourful website with a sense of humour (it needs to dare people to put something bright in their homes).
• Please Note: I don't need a whole website, I have one of my staff who can do that for me. I just want the creative template for the homepage and a standard template for the product pages. It is the graphic design and creative side I am more interested in. I will want my staff member to be able to take the design and incorporate it into the website.

```html
<!DOCTYPE html>
<html lang="en">
<head>
<meta charset="utf-8">
<title>Brassy Walrus – Home</title>
<link href="https://fonts.googleapis.com/css2?family=Pacifico&family=Source+Sans+3:ital,wght@0,400;0,700;1,700&display=swap" rel="stylesheet">
<style>
  :root {
    --page-pink: #c4285a;
    --page-pink-dark: #ad1f4d;
    --paper: #ffffff;
    --body-text: #4a4a4a;
    --lime: #acd036;
    --lime-soft: #cfe38a;
    --sky: #33a6d7;
    --sky-soft: #8ccbe6;
    --teal-ink: #14486a;
    --cart-red: #b5173f;
    --magenta-band: #b73a86;
    --stripe: #e3e3e3;
  }
  * { box-sizing: border-box; margin: 0; padding: 0; }
  html, body { width: 1152px; height: 1200px; overflow: hidden; }
  body {
    position: relative;
    background: radial-gradient(circle at 50% 40%, var(--page-pink) 0%, var(--page-pink-dark) 100%);
    font-family: "Source Sans 3", "Source Sans Pro", sans-serif;
  }
  .page {
    position: absolute; left: 108px; top: 0; width: 936px; height: 1200px;
    background: var(--paper); overflow: hidden;
  }
  .intro p {
    position: absolute; left: 12px; width: 914px;
    font-size: 12px; line-height: 15.3px; color: var(--body-text); text-align: justify;
  }
  .intro .cut { bottom: auto; top: -22px; }
  .intro .full { top: 56px; }

  .section-title {
    position: absolute; left: 10px; top: 160px;
    font-family: "Pacifico", cursive; font-size: 30px; color: var(--lime); line-height: 1.2;
  }
  .title-rule {
    position: absolute; left: 277px; top: 176px; width: 649px; height: 13px;
    background: repeating-linear-gradient(135deg, var(--stripe) 0 2px, transparent 2px 5px);
  }

  .product { position: absolute; width: 220px; }
  .product .photo { width: 220px; height: 190px; position: relative; }
  .product h3 {
    font-weight: 400; font-size: 19px; color: var(--sky); margin-top: 7px; line-height: 24px;
  }
  .product p { font-size: 12px; line-height: 15.3px; color: var(--body-text); margin-top: 6px; padding-left: 1px; }

  .quick-actions .cart-btn {
    position: absolute; left: 24px; top: 51px; width: 172px; height: 45px;
    background: var(--cart-red); border-bottom: 3px solid #8c0f2f;
    color: #fff; font-weight: 700; font-size: 14px;
    display: flex; align-items: center; justify-content: center; gap: 6px;
  }
  .quick-actions .link {
    position: absolute; left: 38px; color: #fff; font-weight: 700; font-size: 14px;
    display: flex; align-items: center; gap: 9px;
  }

  .promo {
    position: absolute; left: 0; top: 876px; width: 936px; height: 270px;
    background: linear-gradient(180deg, #f1efec 0%, #e6e3df 55%, #8e8b88 100%);
  }
  .promo .sofa-shade {
    position: absolute; left: 0; bottom: 0; width: 100%; height: 120px;
    background: linear-gradient(90deg, #e8622e 0%, #d9cfc6 45%, #b0a9a2 75%, #6d6a67 100%);
    opacity: .55;
  }
  .promo .dark-edge { position: absolute; right: 0; top: 0; width: 98px; height: 270px; background: #3a3735; }
  .promo .question {
    position: absolute; left: 0; top: 30px; width: 375px; height: 68px;
    background: rgba(140, 203, 230, .92);
    font-family: "Pacifico", cursive; font-size: 21px; line-height: 28px; color: var(--teal-ink);
    padding: 4px 0 0 26px;
  }
  .promo .answer {
    position: absolute; left: 0; top: 108px; width: 277px; height: 34px;
    background: rgba(207, 227, 138, .95);
    font-weight: 700; font-style: italic; font-size: 21px; line-height: 34px; color: #2f3a10;
    padding-left: 26px;
  }
  .testimonials {
    position: absolute; left: 0; top: 1146px; width: 936px; height: 60px; background: var(--magenta-band);
  }
  .testimonials h2 {
    position: absolute; left: 0; width: 100%; top: 38px; text-align: center;
    font-family: "Pacifico", cursive; font-weight: 400; font-size: 30px; color: #fff; line-height: 1.2;
  }
</style>
</head>
<body>
<main class="page">
  <section class="intro">
    <p class="cut">There are many variations of passages of Lorem Ipsum available, but the majority have suffered alteration in some form, by injected humour, or randomised words which don't look even slightly believable. If you are going to use a passage of Lorem Ipsum, you need to be sure there isn't anything embarrassing hidden in the middle of text. All the Lorem Ipsum generators on the Internet tend to repeat predefined chunks as necessary, making this the first true generator on the Internet. It uses a dictionary of over 200 Latin words, combined with a handful of model sentence structures, to generate Lorem Ipsum which looks reasonable. The generated Lorem Ipsum is therefore always free from repetition, injected humour, or non-characteristic words etc.</p>
    <p class="full">There are many variations of passages of Lorem Ipsum available, but the majority have suffered alteration in some form, by injected humour, or randomised words which don't look even slightly believable. If you are going to use a passage of Lorem Ipsum, you need to be sure there isn't anything embarrassing hidden in the middle of text. All the Lorem Ipsum generators on the Internet tend to repeat predefined chunks as necessary, making this the first true generator on the Internet. It uses a dictionary of over 200 Latin words, combined with a handful of model sentence structures, to generate Lorem Ipsum which looks reasonable. The generated Lorem Ipsum is therefore always free from repetition, injected humour, or non-characteristic words etc.</p>
  </section>

  <h2 class="section-title">Some of our Products</h2>
  <div class="title-rule"></div>

  <article class="product" style="left:11px;top:224px">
    <div class="photo" role="img" aria-label="Blue chinoiserie wallpaper product photo" style="background:linear-gradient(160deg,#5ab9d6,#3fa6cb)">
      <div class="quick-actions">
        <div class="cart-btn">Add To Cart
          <svg width="30" height="24" viewBox="0 0 30 24" fill="none" stroke="#fff" stroke-width="2"><path d="M1 2h5l4 13h15l3-10H8"/><path d="M11 8h15M12 11h13"/><circle cx="12" cy="20" r="2" fill="#fff"/><circle cx="23" cy="20" r="2" fill="#fff"/></svg>
        </div>
        <div class="link" style="top:105px;left:42px">
          <svg width="28" height="24" viewBox="0 0 28 24"><path d="M14 23C4 15 0 11 0 6.5 0 3 3 0 7 0c3 0 5 2 7 4 2-2 4-4 7-4 4 0 7 3 7 6.5C28 11 24 15 14 23z" fill="#fff"/></svg>
          Add To Wishlist</div>
        <div class="link" style="top:141px">
          <svg width="28" height="20" viewBox="0 0 28 20" stroke="#fff" stroke-width="2"><path d="M0 2h28M0 10h28M0 18h28"/></svg>
          Compare Product</div>
      </div>
    </div>
    <h3>Product 1</h3>
    <p>Contrary to popular belief, Lorem Ipsum is not simply random text. It has roots in a piece of classical Latin literature from 45 BC, making it over 2000 years old.</p>
  </article>

  <article class="product" style="left:243px;top:224px">
    <div class="photo" role="img" aria-label="Bright illustrated print with red dancer and green foliage" style="background:linear-gradient(120deg,#5c8a2c 0%,#f2efe9 40%,#d8283c 65%,#f4f1ee 100%)"></div>
    <h3>Product 2</h3>
    <p>Contrary to popular belief, Lorem Ipsum is not simply random text. It has roots in a piece of classical Latin literature from 45 BC, making it over 2000 years old.</p>
  </article>

  <article class="product" style="left:474px;top:224px">
    <div class="photo" role="img" aria-label="Blue and white ginger jar on gilded table" style="background:linear-gradient(90deg,#b08a3e 0%,#3d62b3 25%,#e8ecf4 50%,#3d62b3 75%,#b08a3e 100%)"></div>
    <h3>Product 3</h3>
    <p>Contrary to popular belief, Lorem Ipsum is not simply random text. It has roots in a piece of classical Latin literature from 45 BC, making it over 2000 years old.</p>
  </article>

  <article class="product" style="left:706px;top:224px">
    <div class="photo" role="img" aria-label="White living room with striped animal sculpture" style="background:linear-gradient(120deg,#e9e8e6 0%,#f5f5f3 50%,#7d786f 100%)"></div>
    <h3>Product 4</h3>
    <p>Contrary to popular belief, Lorem Ipsum is not simply random text. It has roots in a piece of classical Latin literature from 45 BC, making it over 2000 years old.</p>
  </article>

  <article class="product" style="left:11px;top:546px">
    <div class="photo" role="img" aria-label="Fireplace with pink trellis wallpaper and mirror" style="background:linear-gradient(180deg,#e56aa3 0%,#f3f0ee 50%,#d8487f 100%)"></div>
    <h3>Product 5</h3>
    <p>Contrary to popular belief, Lorem Ipsum is not simply random text. It has roots in a piece of classical Latin literature from 45 BC, making it over 2000 years old.</p>
  </article>

  <article class="product" style="left:243px;top:546px">
    <div class="photo" role="img" aria-label="Magenta quatrefoil patterned canvas" style="background:linear-gradient(#fff,#fff) padding-box;border:solid #fff;border-width:17px 16px 0 18px"><div style="width:100%;height:100%;background:#dc5fcf"></div></div>
    <h3>Product 6</h3>
    <p>Contrary to popular belief, Lorem Ipsum is not simply random text. It has roots in a piece of classical Latin literature from 45 BC, making it over 2000 years old.</p>
  </article>

  <article class="product" style="left:474px;top:546px">
    <div class="photo" role="img" aria-label="Yellow wicker peacock chair against pink floral wall" style="background:linear-gradient(90deg,#e9e4e2 0%,#ec3f7f 30%,#f1df2a 60%,#d23b6a 100%)"></div>
    <h3>Product 7</h3>
    <p>Contrary to popular belief, Lorem Ipsum is not simply random text. It has roots in a piece of classical Latin literature from 45 BC, making it over 2000 years old.</p>
  </article>

  <article class="product" style="left:706px;top:546px">
    <div class="photo" role="img" aria-label="Pink roses in blue and white vase on trellis wallpaper" style="background:linear-gradient(180deg,#f1a6c8 0%,#7aa84a 35%,#2a4a9c 80%,#e66aa5 100%)"></div>
    <h3>Product 8</h3>
    <p>Contrary to popular belief, Lorem Ipsum is not simply random text. It has roots in a piece of classical Latin literature from 45 BC, making it over 2000 years old.</p>
  </article>

  <section class="promo" role="img" aria-label="Grey sofa piled with orange, white and knitted cushions">
    <div class="sofa-shade"></div>
    <div class="dark-edge"></div>
    <div class="question">Are regretting what you have done<br>with the last 20 years of your life?</div>
    <div class="answer">Then this site is for you!</div>
  </section>

  <section class="testimonials">
    <h2>What Clients Say</h2>
  </section>
</main>
</body>
</html>
```